Larkspur Realty

Business cards for 4 people

They need to say for all
57 Danner Quay, Boston MA 02117

Each person will have their own personal information
We would like gold embossing for the name of the company
Mabel is the blonde sitting in the chair smiling her information should be on the back of the card with her name and information
Should say for slogan classic pattern, elevated experience
mabel@larkspurhomesnet.com
(413) 555-0182

Odessa is the brunette with wavy hair in the tan suit odessa@larkspurhomesnet.com
(617) 555-0147

june@larkspurhomesnet.com
(413) 555-0169
standing next to the chair

ruth@larkspurhomesnet.com
(413) 555-0193
close up headshot

```html
<!DOCTYPE html>
<html lang="en">
<head>
<meta charset="utf-8">
<title>Larkspur Realty — Business Cards</title>
<link rel="stylesheet" href="https://fonts.googleapis.com/css2?family=Cinzel:wght@500&family=Montserrat:wght@400;500&display=swap">
<style>
  :root {
    --page: #ecebe8;
    --navy: #22324f;
    --gold: #e6ad4e;
    --gold-soft: #f5deb3;
    --ink: #1d1d1f;
    --paper: #ffffff;
    --photo-top: #c89a6c;
    --photo-bottom: #8a6040;
  }
  * { box-sizing: border-box; margin: 0; padding: 0; }
  html, body { width: 1200px; height: 1108px; overflow: hidden; }
  body {
    background: var(--page);
    display: flex;
    flex-direction: column;
    align-items: center;
    justify-content: center;
    gap: 60px;
    font-family: "Montserrat", Arial, sans-serif;
  }
  .card {
    width: 800px;
    height: 457px;
    position: relative;
    overflow: hidden;
    box-shadow: 0 6px 18px rgba(0,0,0,0.18);
  }
  .wordmark-name {
    font-family: "Cinzel", Georgia, serif;
    font-weight: 500;
    color: var(--gold);
    letter-spacing: 0.04em;
    line-height: 1;
    white-space: nowrap;
  }

  /* Front */
  .card-front { background: var(--navy); }
  .emblem-ring {
    position: absolute;
    left: 390px;
    top: -30px;
    width: 340px;
    height: 340px;
    border: 13px solid var(--gold);
    border-radius: 50%;
  }
  .card-front .wordmark {
    position: absolute;
    left: 60px;
    bottom: 60px;
  }
  .card-front .wordmark-name { font-size: 52px; }
  .slogan {
    margin-top: 14px;
    font-size: 15px;
    font-weight: 500;
    color: var(--gold);
    letter-spacing: 0.32em;
    text-transform: uppercase;
  }

  /* Back */
  .card-back { background: var(--paper); }
  .ghost-ring {
    position: absolute;
    left: 440px;
    top: 50px;
    width: 320px;
    height: 320px;
    border: 14px solid var(--gold-soft);
    border-radius: 50%;
  }
  .card-back .wordmark {
    position: absolute;
    left: 50px;
    top: 50px;
    display: flex;
    align-items: center;
    gap: 14px;
  }
  .wordmark-dot {
    width: 32px; height: 32px;
    border: 2px solid var(--gold);
    border-radius: 50%;
    flex: none;
  }
  .card-back .wordmark-name { font-size: 30px; }

  .agent {
    position: absolute;
    left: 50px;
    top: 160px;
  }
  .agent-name {
    font-family: "Cinzel", Georgia, serif;
    font-weight: 500;
    font-size: 36px;
    color: var(--gold);
    letter-spacing: 0.03em;
    line-height: 1;
  }
  .agent-role {
    display: inline-block;
    margin-top: 6px;
    padding: 0 40px 6px 0;
    font-size: 18px;
    font-weight: 500;
    color: var(--ink);
    border-bottom: 2px solid var(--gold);
  }
  .address {
    position: absolute;
    left: 50px;
    top: 272px;
    font-size: 18px;
    line-height: 1.3;
    color: var(--ink);
  }
  .contact {
    position: absolute;
    left: 50px;
    top: 350px;
    list-style: none;
    font-size: 18px;
    color: var(--ink);
  }
  .contact li { display: flex; align-items: center; gap: 14px; line-height: 1.45; }
  .contact svg { width: 18px; height: 18px; fill: var(--gold); flex: none; }

  .agent-photo {
    position: absolute;
    right: 0;
    top: 40px;
    width: 300px;
    height: 417px;
    border-radius: 140px 0 0 0;
    background: linear-gradient(180deg, var(--photo-top), var(--photo-bottom));
  }
</style>
</head>
<body>

  <section class="card card-front">
    <span class="emblem-ring"></span>
    <div class="wordmark">
      <p class="wordmark-name">LARKSPUR REALTY</p>
      <p class="slogan">Classic pattern, elevated experience</p>
    </div>
  </section>

  <section class="card card-back">
    <span class="ghost-ring"></span>

    <div class="wordmark">
      <span class="wordmark-dot"></span>
      <span class="wordmark-name">LARKSPUR REALTY</span>
    </div>

    <div class="agent">
      <h1 class="agent-name">MABEL ASHBY</h1>
      <p class="agent-role">Real Estate Agent</p>
    </div>

    <p class="address">57 Danner Quay<br>Boston MA 02117</p>

    <ul class="contact">
      <li>
        <svg viewBox="0 0 24 24" aria-hidden="true"><path d="M6.6 10.8a15.1 15.1 0 0 0 6.6 6.6l2.2-2.2c.3-.3.7-.4 1-.2 1.1.4 2.3.6 3.6.6.6 0 1 .4 1 1V20c0 .6-.4 1-1 1A17 17 0 0 1 3 4c0-.6.4-1 1-1h3.5c.6 0 1 .4 1 1 0 1.3.2 2.5.6 3.6.1.3 0 .7-.2 1z"/></svg>
        (413) 555-0182
      </li>
      <li>
        <svg viewBox="0 0 24 24" aria-hidden="true"><path d="M2 5h20v14H2z M3.5 6.5 12 13l8.5-6.5" stroke="#fff" stroke-width="1.6"/></svg>
        mabel@larkspurhomesnet.com
      </li>
    </ul>

    <div class="agent-photo" role="img" aria-label="Portrait of Mabel Ashby seated in a wooden chair, wearing a tan suit"></div>
  </section>

</body>
</html>
```